KTR Engineering Pty Ltd

I have already had Corvale welding and fabrication cards made , my business has changed too KTR engineering Pty Ltd so I need my logo changed on the cards
one side have my logo then the other side have what we do.
front side logo and details
owner /operator : Lachlan Meravic
email: ktr.works@ironvalemail.com
number: 0491537204
ABN: 47 261 538 902
ACN: 718 352 946
on back have in dot points what we do:
* structural steel erection
* precast panels
* site welding
*steel alteration & repair
* rigging & dogging
*labour hire
all details in breif

```html
<!DOCTYPE html>
<html lang="en">
<head>
<meta charset="utf-8">
<title>KTR Engineering Pty Ltd – Business Cards</title>
<link rel="stylesheet" href="https://fonts.googleapis.com/css2?family=Montserrat:wght@500;600;700;800;900&display=swap">
<style>
  :root {
    --navy: #17223a;
    --navy-deep: #0f1729;
    --navy-card: #1b2742;
    --red: #a8443d;
    --silver-light: #f4f5f7;
    --silver-mid: #dcdee3;
    --white: #ffffff;
    --page: #e9eaee;
    --muted: #c9cdd6;
  }
  * { box-sizing: border-box; margin: 0; padding: 0; }
  html, body {
    width: 1200px; height: 800px; overflow: hidden;
    background: var(--page);
    font-family: "Montserrat", Arial, sans-serif;
  }
  .canvas {
    width: 1200px; height: 800px;
    display: flex; align-items: center; justify-content: center; gap: 30px;
  }
  .card {
    position: relative; width: 560px; height: 320px;
    border-radius: 18px; overflow: hidden;
    box-shadow: 0 10px 30px rgba(15, 23, 41, .25);
  }

  /* ---------- Services side ---------- */
  .card--services {
    background: radial-gradient(circle at 45% 35%, #24335a 0%, var(--navy-card) 55%, var(--navy-deep) 100%);
    color: var(--white);
  }
  .brand {
    position: absolute; display: flex; align-items: center; gap: 10px;
  }
  .brand__mark {
    width: 14px; height: 14px; border-radius: 50%; background: var(--red); flex: none;
  }
  .brand__name {
    font-weight: 900; font-size: 26px; line-height: 1.05; letter-spacing: .5px;
    text-transform: uppercase;
  }
  .card--services .brand { left: 40px; top: 40px; }
  .card--services .brand__name { color: var(--white); }
  .brand-phone {
    position: absolute; font-weight: 700; font-size: 11px; letter-spacing: 1px; color: var(--red);
  }
  .card--services .brand-phone { left: 64px; top: 104px; }

  .services {
    position: absolute; left: 40px; right: 40px; top: 150px;
    display: grid; grid-template-columns: 1fr 1fr; column-gap: 36px;
    list-style: none;
  }
  .services__item {
    position: relative; padding: 10px 0 7px 20px;
    font-weight: 700; font-size: 12.5px; letter-spacing: .6px; text-transform: uppercase;
    border-bottom: 1px solid var(--muted);
  }
  .services__item::before {
    content: ""; position: absolute; left: 2px; top: 14px;
    width: 8px; height: 8px; border-radius: 50%; background: var(--white);
  }

  /* ---------- Details side ---------- */
  .card--details { background: var(--navy); }
  .card__bg { position: absolute; inset: 0; width: 100%; height: 100%; }
  .card--details .brand { left: 34px; top: 118px; }
  .card--details .brand__name { color: var(--navy); font-size: 24px; }
  .card--details .brand-phone { left: 58px; top: 178px; }

  .person { position: absolute; left: 34px; top: 206px; }
  .person__name {
    font-weight: 800; font-size: 17px; letter-spacing: 1px; color: var(--navy); text-transform: uppercase;
  }
  .person__role {
    font-weight: 700; font-size: 12px; letter-spacing: 1px; color: var(--red); text-transform: uppercase; margin-top: 2px;
  }
  .contact { list-style: none; margin-top: 10px; }
  .contact__item {
    display: flex; align-items: center; gap: 8px;
    font-weight: 600; font-size: 12.5px; color: var(--navy); margin-top: 4px;
  }
  .contact__icon { width: 16px; height: 16px; flex: none; }

  .rule {
    position: absolute; height: 1.5px; background: var(--red);
  }
  .rule--name { left: 250px; top: 214px; width: 120px; }

  .company-ids { position: absolute; right: 108px; top: 150px; text-align: left; }
  .company-ids__rule { height: 3px; width: 140px; background: var(--navy); margin-bottom: 8px; }
  .company-ids__line { font-weight: 600; font-size: 12px; color: var(--navy); letter-spacing: .3px; margin-top: 2px; }
  .company-ids__label { color: var(--red); font-weight: 800; }
</style>
</head>
<body>
<main class="canvas">

  <!-- Services side -->
  <section class="card card--services" aria-label="Card back: services">
    <div class="brand">
      <span class="brand__mark"></span>
      <span class="brand__name">KTR Engineering<br>Pty Ltd</span>
    </div>
    <span class="brand-phone">0491537204</span>
    <ul class="services">
      <li class="services__item">Structural steel erection</li>
      <li class="services__item">Steel alteration &amp; repair</li>
      <li class="services__item">Precast panels</li>
      <li class="services__item">Rigging &amp; dogging</li>
      <li class="services__item">Site welding</li>
      <li class="services__item">Labour hire</li>
    </ul>
  </section>

  <!-- Details side -->
  <section class="card card--details" aria-label="Card front: contact details">
    <svg class="card__bg" viewBox="0 0 560 320" preserveAspectRatio="none" aria-hidden="true">
      <defs>
        <linearGradient id="brushed" x1="0" y1="0" x2="1" y2="1">
          <stop offset="0" stop-color="#ffffff"/>
          <stop offset=".5" stop-color="#eceef1"/>
          <stop offset="1" stop-color="#d9dce1"/>
        </linearGradient>
      </defs>
      <path d="M0,320 L0,150 C150,66 340,48 560,92 L560,320 Z" fill="url(#brushed)"/>
      <path d="M0,134 C150,50 340,32 560,76 L560,92 C340,48 150,66 0,150 Z" fill="#a8443d"/>
      <rect x="476" y="196" width="84" height="124" fill="#a8443d"/>
      <path d="M250,320 L476,320 L476,298 L282,298 Z" fill="#17223a"/>
    </svg>

    <div class="brand">
      <span class="brand__mark"></span>
      <span class="brand__name">KTR Engineering<br>Pty Ltd</span>
    </div>
    <span class="brand-phone">0491537204</span>

    <span class="rule rule--name"></span>

    <div class="person">
      <p class="person__name">Lachlan Meravic</p>
      <p class="person__role">Owner / Operator</p>
      <ul class="contact">
        <li class="contact__item">
          <svg class="contact__icon" viewBox="0 0 16 16" aria-hidden="true">
            <rect width="16" height="16" rx="2" fill="#a8443d"/>
            <path d="M5 3.5l2 2-1 1.5c.6 1.3 1.7 2.4 3 3l1.5-1 2 2-1.2 1.5C7.8 12.3 3.7 8.2 3.5 4.7Z" fill="#fff"/>
          </svg>
          0491537204
        </li>
        <li class="contact__item">
          <svg class="contact__icon" viewBox="0 0 16 16" aria-hidden="true">
            <rect width="16" height="16" rx="2" fill="#a8443d"/>
            <rect x="3" y="4.5" width="10" height="7" fill="none" stroke="#fff" stroke-width="1.2"/>
            <path d="M3 4.5l5 4 5-4" fill="none" stroke="#fff" stroke-width="1.2"/>
          </svg>
          ktr.works@ironvalemail.com
        </li>
      </ul>
    </div>

    <div class="company-ids">
      <div class="company-ids__rule"></div>
      <p class="company-ids__line"><span class="company-ids__label">ABN:</span> 47 261 538 902</p>
      <p class="company-ids__line"><span class="company-ids__label">ACN:</span> 718 352 946</p>
    </div>
  </section>

</main>
</body>
</html>
```